Business Card - Cooperate

Business Card for Larkfield Management Consulting

Target Market(s)

Corparte - b2B

Industry/Entity Type

Management Consulting - Professional Services

Contact Information for Business Card

Company Name , Slogan , Dummy Address,

Requirements
Must have
• Reach your Full Potential

```html
<!DOCTYPE html>
<html lang="en">
<head>
<meta charset="utf-8">
<title>Larkfield Management Consulting – Business Card</title>
<link href="https://fonts.googleapis.com/css2?family=Comfortaa:wght@400;700&display=swap" rel="stylesheet">
<style>
  :root {
    --backdrop: #dfece7;
    --card: #ffffff;
    --brand-blue: #2f4fae;
    --brand-mark: #3d76c9;
    --body-text: #5a6b86;
    --panel-top: #1e3f85;
    --panel-mid: #0b6685;
    --panel-bottom: #7fc14d;
    --panel-text: #ffffff;
  }
  * { box-sizing: border-box; margin: 0; padding: 0; }
  html, body {
    width: 1200px; height: 800px; overflow: hidden;
    background: var(--backdrop);
  }
  .canvas { position: relative; width: 1200px; height: 800px; }

  .card {
    position: absolute;
    width: 500px; height: 286px;
    background: var(--card);
    border-radius: 16px;
    overflow: hidden;
    box-shadow: 0 10px 24px rgba(40, 70, 60, 0.16);
  }
  .card--front { left: 620px; top: 100px; }
  .card--back { left: 80px; top: 410px; }

  .brand { position: absolute; display: flex; align-items: center; gap: 12px; }
  .brand__dot {
    width: 38px; height: 38px; border-radius: 50%;
    background: var(--brand-mark);
  }
  .brand__name {
    font-family: "Comfortaa", sans-serif; font-weight: 700;
    font-size: 44px; color: var(--brand-blue); letter-spacing: 0.5px;
    line-height: 1;
  }
  .card--front .brand { left: 78px; top: 112px; }

  .card__slogan {
    position: absolute;
    font-family: "Comfortaa", sans-serif; font-weight: 400;
    color: var(--body-text);
  }
  .card--front .card__slogan { left: 0; right: 0; bottom: 34px; text-align: center; font-size: 13px; }

  .card--back .brand { left: 24px; top: 118px; gap: 8px; }
  .card--back .brand__dot { width: 24px; height: 24px; }
  .card--back .brand__name { font-size: 28px; }
  .card--back .card__slogan { left: 0; width: 250px; bottom: 26px; text-align: center; font-size: 10px; }

  .contact-panel {
    position: absolute; left: 250px; top: 0; width: 250px; height: 100%;
    background: linear-gradient(180deg, var(--panel-top) 0%, var(--panel-mid) 45%, var(--panel-bottom) 100%);
    color: var(--panel-text);
    font-family: "Comfortaa", sans-serif;
    padding: 38px 20px 0 24px;
  }
  .contact-panel__name {
    font-weight: 700; font-size: 20px; letter-spacing: 1px;
    margin-bottom: 26px; text-align: center;
  }
  .contact-list { list-style: none; }
  .contact-list__item {
    display: flex; align-items: center; gap: 12px;
    font-size: 11.5px; margin-bottom: 18px; white-space: nowrap;
  }
  .contact-list__icon { width: 14px; height: 14px; flex: none; }
</style>
</head>
<body>
<main class="canvas">

  <section class="card card--front" aria-label="Business card front">
    <div class="brand">
      <span class="brand__dot"></span>
      <span class="brand__name">Larkfield</span>
    </div>
    <p class="card__slogan">Reach your full potential</p>
  </section>

  <section class="card card--back" aria-label="Business card back">
    <div class="brand">
      <span class="brand__dot"></span>
      <span class="brand__name">Larkfield</span>
    </div>
    <p class="card__slogan">Reach your full potential</p>

    <div class="contact-panel">
      <p class="contact-panel__name">Alex Morgan</p>
      <ul class="contact-list">
        <li class="contact-list__item">
          <svg class="contact-list__icon" viewBox="0 0 16 16" fill="#fff"><path d="M8 1a5 5 0 0 0-5 5c0 4 5 9 5 9s5-5 5-9a5 5 0 0 0-5-5zm0 7a2 2 0 1 1 0-4 2 2 0 0 1 0 4z"/></svg>
          14 Elm Row, Westbury
        </li>
        <li class="contact-list__item">
          <svg class="contact-list__icon" viewBox="0 0 16 16" fill="none" stroke="#fff" stroke-width="1.4"><rect x="4" y="1" width="8" height="14" rx="1.5"/><line x1="7" y1="12.5" x2="9" y2="12.5"/></svg>
          +1 555 0148 2290
        </li>
        <li class="contact-list__item">
          <svg class="contact-list__icon" viewBox="0 0 16 16" fill="none" stroke="#fff" stroke-width="1.4"><rect x="1" y="3" width="14" height="10" rx="1"/><path d="M1 3l7 6 7-6"/></svg>
          hello@larkfieldmc.com
        </li>
        <li class="contact-list__item">
          <svg class="contact-list__icon" viewBox="0 0 16 16" fill="none" stroke="#fff" stroke-width="1.2"><circle cx="8" cy="8" r="6.5"/><ellipse cx="8" cy="8" rx="3" ry="6.5"/><line x1="1.5" y1="8" x2="14.5" y2="8"/></svg>
          www.larkfieldmc.com
        </li>
      </ul>
    </div>
  </section>

</main>
</body>
</html>
```